Velunor chemicals

We need a clean web design for a new e-commerce site selling Natural bio degrader products , please see attached docs

Industry/Entity Type

Graphic Design

```html
<!DOCTYPE html>
<html lang="en">
<head>
<meta charset="utf-8">
<title>Velunor chemicals – Store</title>
<link rel="stylesheet" href="https://fonts.googleapis.com/css2?family=Lato:wght@400;700&display=swap">
<style>
:root{
  --bg:#ffffff;
  --line:#e3e3e3;
  --text:#333333;
  --muted:#8a8a8a;
  --green:#7cb342;
  --lime:#a8c23a;
  --star:#f2b01e;
  --footer:#3b3b3b;
  --footer-top:#2e2e2e;
  --bottom:#2b2b2b;
  --footer-text:#dcdcdc;
  --footer-muted:#8c8c8c;
  --thumb-a:#6e7a5c;
  --thumb-b:#7a6446;
}
*{box-sizing:border-box;margin:0;padding:0}
html,body{width:1200px;height:927px;overflow:hidden;background:var(--bg)}
body{font-family:'Lato',Arial,sans-serif;color:var(--text)}
.page{position:relative;width:1160px;height:896px;transform:scale(1.03448);transform-origin:0 0}
.abs{position:absolute}

.tabs{left:75px;top:14px;width:751px;height:33px;border-bottom:1px solid var(--line)}
.tab{position:absolute;top:0;height:33px;line-height:33px;font-size:12px;color:var(--muted)}
.tab--active{left:0;width:56px;text-align:center;color:var(--text);background:#fff;border:1px solid var(--line);border-left:3px solid var(--lime);border-bottom-color:#fff}

.card{top:64px;width:176px;height:246px;border:1px solid var(--line);background:#fff}
.card__media{position:absolute;left:30px;top:20px;width:114px;height:136px;border-radius:4px}
.card__badge{position:absolute;right:14px;top:14px;width:35px;height:35px;background:var(--green);color:#fff;font-size:10px;font-weight:700;line-height:35px;text-align:center}
.card__title{position:absolute;top:179px;width:100%;text-align:center;font-size:12.5px;color:#333}
.card__price{position:absolute;top:196px;width:100%;text-align:center;font-size:12px;color:var(--lime)}
.card__price s{color:var(--muted);margin-right:3px}
.card__stars{position:absolute;top:213px;left:0;width:100%;text-align:center;font-size:15px;color:var(--star);line-height:16px}
.card__stars .off{color:#bbb}

.note{left:851px;top:0;width:1px;height:156px;background:var(--line)}
.note-inner{left:887px;top:38px;width:1px;height:122px;background:var(--line)}
.note-title{left:905px;top:15px;font-size:12px;font-weight:700;color:#222}
.note-icon{left:880px;top:16px}
.note-text{left:905px;top:39px;width:180px;font-size:11.5px;line-height:17.3px;color:#555}

.section-tab{height:36px;line-height:36px;padding-left:18px;font-size:16px;color:#666;background:#fff;border:1px solid var(--line);border-left:3px solid var(--lime);border-bottom-color:#fff}
.brands-line{left:75px;top:379px;width:665px;height:1px;background:var(--line)}
.brands{left:75px;top:397px;width:665px;height:172px;border:1px solid var(--line);display:grid;grid-template-columns:repeat(5,1fr);grid-template-rows:repeat(2,1fr)}
.brand{display:flex;align-items:center;justify-content:center;border-right:1px solid var(--line);border-bottom:1px solid var(--line);font-size:24px;color:#c9c9c9;letter-spacing:-.3px}
.brand:nth-child(5n){border-right:none}
.brand:nth-child(n+6){border-bottom:none}

.testi-title{left:766px;top:353px;font-size:16px;color:#333}
.testi-arrows{left:1053px;top:356px}
.testi{left:766px;top:379px;width:320px;height:193px;border:1px solid var(--line);padding:10px 9px;font-size:11.5px;line-height:17.5px;color:var(--muted)}
.testi p{margin-bottom:9px}
.testi cite{display:block;text-align:right;font-style:normal;color:#444;margin-top:16px;padding-right:16px}

.footer{left:0;top:615px;width:1160px;height:229px;background:var(--footer);border-top:7px solid var(--footer-top)}
.fcol{top:650px}
.fcol h3{font-size:15.5px;font-weight:400;color:var(--footer-text);margin-bottom:8px}
.fcol a{display:block;font-size:12px;line-height:17.4px;color:var(--footer-text);text-decoration:underline}
.news-line{left:766px;width:320px;height:0;border-top:1px dotted #777}
.news-thumb{left:766px;width:48px;height:48px;border:2px solid #555}
.news-title{left:822px;font-size:12px;color:var(--footer-text)}
.news-date{left:822px;font-size:11px;color:var(--footer-muted)}

.bottom{left:0;top:844px;width:1160px;height:52px;background:var(--bottom)}
.search{left:75px;top:857px;width:223px;height:26px;border:1px solid #555;background:#3a3a3a;font-size:11px;color:#999;line-height:24px;padding-left:6px}
.search svg{position:absolute;right:6px;top:6px}
.social-label{left:315px;top:863px;font-size:12px;color:#bbb}
.social{top:857px;width:26px;height:26px;border-radius:50%;background:#d8d8d8}
.bottom-links{left:705px;top:863px;font-size:12px;color:#bbb;display:flex}
.bottom-links a{color:#bbb;text-decoration:underline;padding:0 9px;border-left:1px solid #666}
.bottom-links a:first-child{padding-left:0;border-left:none}
.bottom-links span{padding-left:9px;border-left:1px solid #666}
.bottom-links span a{border:none;padding:0}
</style>
</head>
<body>
<div class="page">

  <nav class="abs tabs">
    <span class="tab tab--active">Lorem</span>
    <span class="tab" style="left:69px">Lorem</span>
    <span class="tab" style="left:125px">Lorem</span>
    <span class="tab" style="left:181px">Lorem</span>
    <span class="tab" style="left:237px">Lorem</span>
  </nav>

  <article class="abs card" style="left:75px">
    <div class="card__media" role="img" aria-label="Blue laundry liquid bottle" style="background:linear-gradient(#ffffff,#cfe7f3)"></div>
    <div class="card__badge">Sale!</div>
    <div class="card__title">Lorem Ipsum Dolor</div>
    <div class="card__price">£14.99–£74.99</div>
    <div class="card__stars">★★★★★</div>
  </article>

  <article class="abs card" style="left:267px">
    <div class="card__media" role="img" aria-label="Green dishwashing liquid bottle" style="background:linear-gradient(#ffffff,#d6ecd8)"></div>
    <div class="card__badge">Sale!</div>
    <div class="card__title">Lorem Ipsum Dolor</div>
    <div class="card__price"><s>£19.99–£59.99</s><u>£14.99–£54.99</u></div>
    <div class="card__stars">★★★<span class="off">☆☆</span></div>
  </article>

  <article class="abs card" style="left:459px">
    <div class="card__media" role="img" aria-label="Group of cleaning product canisters" style="background:linear-gradient(#ffffff,#ebe4d2)"></div>
    <div class="card__badge">Sale!</div>
    <div class="card__price"><s>£79.99</s><u>£74.99</u></div>
    <div class="card__stars">★★★<span class="off">☆☆</span></div>
  </article>

  <article class="abs card" style="left:651px">
    <div class="card__media" role="img" aria-label="Purple floor cleaner bottle" style="background:linear-gradient(#ffffff,#e2d9ee)"></div>
    <div class="card__badge">Sale!</div>
    <div class="card__title">Lorem Ipsum Dolor</div>
    <div class="card__price"><s>£29.99</s><u>£24.99</u></div>
    <div class="card__stars">★★★★★</div>
  </article>

  <div class="abs note"></div>
  <svg class="abs note-icon" width="16" height="12" viewBox="0 0 16 12" aria-hidden="true">
    <rect x="1" y="2" width="9" height="6" fill="none" stroke="#999" stroke-width="1.4"/>
    <path d="M10 4h3l2 2v2h-5z" fill="none" stroke="#999" stroke-width="1.4"/>
    <circle cx="4" cy="9.5" r="1.5" fill="#999"/><circle cx="12" cy="9.5" r="1.5" fill="#999"/>
  </svg>
  <div class="abs note-title">Lorem ipsum dolor</div>
  <div class="abs note-inner"></div>
  <p class="abs note-text">Lorem ipsum dolor sit amet, consectetur adipiscing elit. Sed pulvinar, felis fringillaconvallis rhoncus, lorem arcu feugiat nisi, vel accumsan nisi arcu sit amet metus. Pellentesque id lorem in dolor condimentum varius [...]</p>

  <div class="abs brands-line"></div>
  <h2 class="abs section-tab" style="left:75px;top:345px;width:116px;font-weight:400">Our Brands</h2>
  <div class="abs brands">
    <div class="brand">Norvane</div><div class="brand">Norvane</div><div class="brand">Norvane</div><div class="brand">Norvane</div><div class="brand">Norvane</div>
    <div class="brand">Norvane</div><div class="brand">Norvane</div><div class="brand">Norvane</div><div class="brand">Norvane</div><div class="brand">Norvane</div>
  </div>

  <h2 class="abs testi-title" style="font-weight:400">Testimonial</h2>
  <svg class="abs testi-arrows" width="32" height="12" viewBox="0 0 32 12" aria-hidden="true">
    <path d="M7 1L2 6l5 5M12 1L7 6l5 5" fill="none" stroke="#bbb" stroke-width="1.5"/>
    <path d="M20 1l5 5-5 5M25 1l5 5-5 5" fill="none" stroke="#bbb" stroke-width="1.5"/>
  </svg>
  <blockquote class="abs testi">
    <p>Lorem ipsum dolor sit amet, consectetur adipiscing elit. Nunc in justo eget ipsum sollicitudin mattis. In tincidunt tincidunt convallis. Ut id neque eget ligula dictum auctor. Morbi non nulla augue, ac facilisis risus.</p>
    <p>Praesent rhoncus iaculis enim, vitae condimentum nulla tristique nec. Nulla sit amet quam in neque lacinia molestie. Suspendisse pellentesque iaculis elit id rutrum.</p>
    <cite>John Doe, CEO</cite>
  </blockquote>

  <footer class="abs footer"></footer>

  <div class="abs fcol" style="left:75px"><h3>Shopping Guide</h3><a>How to buy</a><a>FAQ's</a><a>Payment</a><a>Shipment</a><a>Where is my order?</a><a>Return policy</a><a>Terms and conditions</a></div>
  <div class="abs fcol" style="left:238px"><h3>About Us</h3><a>How to buy</a><a>FAQ's</a><a>Payment</a><a>Shipment</a><a>Where is my order?</a><a>Return policy</a><a>Terms and conditions</a></div>
  <div class="abs fcol" style="left:421px"><h3>Style Advisor</h3><a>How to buy</a><a>FAQ's</a><a>Payment</a><a>Shipment</a><a>Where is my order?</a><a>Return policy</a><a>Terms and conditions</a></div>
  <div class="abs fcol" style="left:584px"><h3>Customer Service</h3><a>How to buy</a><a>FAQ's</a><a>Payment</a><a>Shipment</a><a>Where is my order?</a><a>Return policy</a><a>Terms and conditions</a></div>
  <div class="abs fcol" style="left:766px"><h3>Our Lates News</h3></div>

  <div class="abs news-line" style="top:677px"></div>
  <div class="abs news-thumb" style="top:686px;background:var(--thumb-a)" role="img" aria-label="Preview image for the full width post"></div>
  <div class="abs news-title" style="top:688px">Full width post with preview image</div>
  <div class="abs news-date" style="top:706px">11 Apr 2013</div>
  <div class="abs news-line" style="top:742px"></div>
  <div class="abs news-thumb" style="top:752px;background:var(--thumb-b)" role="img" aria-label="Preview image for the link post"></div>
  <div class="abs news-title" style="top:754px">Link post with preview image</div>
  <div class="abs news-date" style="top:772px">11 Apr 2013</div>
  <div class="abs news-line" style="top:808px"></div>

  <div class="abs bottom"></div>
  <div class="abs search">search entire store here
    <svg width="13" height="13" viewBox="0 0 13 13" aria-hidden="true"><circle cx="5.5" cy="5.5" r="4" fill="none" stroke="#999" stroke-width="1.5"/><path d="M8.5 8.5L12 12" stroke="#999" stroke-width="1.8"/></svg>
  </div>
  <div class="abs social-label">Social Media:</div>
  <span class="abs social" style="left:388px"></span>
  <span class="abs social" style="left:418px"></span>
  <span class="abs social" style="left:448px"></span>
  <span class="abs social" style="left:478px"></span>
  <span class="abs social" style="left:508px"></span>

  <div class="abs bottom-links">
    <a>Sitemap</a><a>Home</a><a>About Us</a><a>Contact Us</a>
    <span>Copyright © 2014 <a>VELUNOR</a></span>
  </div>
</div>
</body>
</html>
```